Need Business Cards for my Business

email address: rkpmarlowhollowworks@vendrimail.com
web address: rkpmarlowhollowworks.net
Slogan: We offer various QVN licenses
Rowland K. Pemberly
Please stick with colors of Company Logo
would like the card to be more of the color example of the logo.
If you need PDF copy of logo email me at the above account.
Creative control rests with you.

Industry/Entity Type

Business

Contact Information for Business Card

I am a minimalist, but would like something to pop and stand out amongst other cards, make it memorable.

Font styles to use
Serif
Decorative
Script

```html
<!DOCTYPE html>
<html lang="en">
<head>
<meta charset="utf-8">
<title>Rowland K. Pemberly – Business Cards</title>
<link href="https://fonts.googleapis.com/css2?family=Architects+Daughter&family=Montserrat:wght@500;600;800&display=swap" rel="stylesheet">
<style>
  :root {
    --page: #ffffff;
    --card: #ffffff;
    --name-cyan: #8fe3ef;
    --ink: #111111;
    --brand-blue: #1d4f9e;
    --brand-red: #e2222a;
    --shadow: rgba(0, 0, 0, 0.45);
  }
  html, body {
    margin: 0;
    padding: 0;
    width: 1200px;
    height: 1200px;
    overflow: hidden;
    background: var(--page);
  }
  .canvas {
    position: relative;
    width: 1200px;
    height: 1200px;
  }
  .card {
    position: absolute;
    width: 881px;
    height: 527px;
    background: var(--card);
    box-shadow: 8px 10px 14px var(--shadow);
  }
  .card--front { left: 166px; top: 38px; }
  .card--back  { left: 173px; top: 620px; }

  .holder-name {
    position: absolute;
    top: 72px;
    left: 0;
    width: 100%;
    text-align: center;
    font-family: "Architects Daughter", cursive;
    font-size: 41px;
    color: var(--name-cyan);
    letter-spacing: 1px;
  }
  .monogram {
    position: absolute;
    top: 232px;
    left: 0;
    width: 100%;
    text-align: center;
    font-family: "Montserrat", sans-serif;
    font-weight: 800;
    font-size: 34px;
    color: var(--ink);
  }
  .contact {
    position: absolute;
    top: 404px;
    left: 0;
    width: 100%;
    text-align: center;
    font-family: "Montserrat", sans-serif;
    font-weight: 500;
    font-size: 18.5px;
    line-height: 24px;
    color: var(--ink);
  }
  .contact p { margin: 0; }

  .brand {
    position: absolute;
    top: 170px;
    left: 0;
    width: 100%;
    text-align: center;
  }
  .brand-name {
    display: inline-flex;
    align-items: center;
    gap: 16px;
    font-family: "Montserrat", sans-serif;
    font-weight: 800;
    font-size: 48px;
    color: var(--brand-blue);
    letter-spacing: 0.5px;
  }
  .brand-mark {
    width: 30px;
    height: 30px;
    background: var(--brand-red);
  }
  .slogan {
    margin-top: 14px;
    font-family: "Montserrat", sans-serif;
    font-weight: 600;
    font-size: 21px;
    letter-spacing: 2.5px;
    color: var(--ink);
  }
</style>
</head>
<body>
<main class="canvas">
  <section class="card card--front" aria-label="Business card front">
    <div class="holder-name">Rowland K. Pemberly</div>
    <div class="monogram">RKP</div>
    <div class="contact">
      <p>rkpmarlowhollowworks.net</p>
      <p>rkpmarlowhollowworks@vendrimail.com</p>
    </div>
  </section>

  <section class="card card--back" aria-label="Business card back">
    <div class="brand">
      <div class="brand-name"><span class="brand-mark"></span>RKP Marlow Hollow Works</div>
      <div class="slogan">We Offer Various QVN Licenses</div>
    </div>
  </section>
</main>
</body>
</html>
```